Business Card Design

I would like to have business cards completely redesigned for my car ceramic coating and detailing business.
The cards uploaded are the current, the information needs to change but you can see our logo, I want something modern, professional and eye catching.

```html
<!DOCTYPE html>
<html lang="en">
<head>
<meta charset="utf-8">
<title>Crestline Detail – Business Card</title>
<link href="https://fonts.googleapis.com/css2?family=Roboto:wght@400;500;700&display=swap" rel="stylesheet">
<style>
  :root{
    --card-blue:#3146a3;
    --card-blue-deep:#273a8c;
    --white:#ffffff;
    --soft-white:rgba(255,255,255,.85);
    --stage:#e4e6ea;
  }
  *{box-sizing:border-box;margin:0;padding:0}
  html,body{width:1200px;height:800px;overflow:hidden}
  body{
    background:var(--stage);
    font-family:"Roboto",Arial,sans-serif;
    color:var(--white);
    display:flex;align-items:center;justify-content:center;gap:40px;
  }
  .card{
    position:relative;width:540px;height:309px;
    background:var(--card-blue);border-radius:6px;overflow:hidden;
    box-shadow:0 10px 24px rgba(0,0,0,.18);
  }

  /* back side */
  .brand-block{
    position:absolute;left:34px;top:100px;width:160px;
    display:flex;align-items:center;gap:10px;
  }
  .brand-dot{width:16px;height:16px;border-radius:50%;background:var(--white);flex:none}
  .brand-name{font-weight:700;font-size:22px;line-height:1.1}
  .divider{position:absolute;left:224px;top:40px;width:1px;height:180px;background:var(--soft-white)}
  .contact{position:absolute;right:70px;top:40px;text-align:right}
  .contact__name{font-size:22px;font-weight:700}
  .contact__role{font-size:12px;margin-top:4px;display:inline-block;border-bottom:2px solid var(--white);padding-bottom:2px}
  .contact__trade{font-size:12px;margin-top:4px}
  .contact__phone{font-size:13px;margin-top:44px}
  .contact__email{font-size:13px;margin-top:28px}
  .icon-rail{position:absolute;right:22px;top:38px;width:32px;height:160px}
  .address{position:absolute;left:30px;bottom:28px;font-size:12px;display:flex;align-items:center;gap:8px}

  /* front side */
  .front-brand{
    position:absolute;left:0;right:0;top:92px;
    display:flex;align-items:center;justify-content:center;gap:16px;
  }
  .front-brand .brand-dot{width:24px;height:24px}
  .front-brand .brand-name{font-size:46px}
  .wave{position:absolute;left:0;bottom:0;width:540px;height:140px}
</style>
</head>
<body>

<section class="card card--back">
  <div class="brand-block">
    <span class="brand-dot"></span>
    <span class="brand-name">Crestline Detail</span>
  </div>
  <div class="divider"></div>

  <div class="contact">
    <div class="contact__name">Jordan Ellery</div>
    <div class="contact__role">Owner | Operator</div>
    <div class="contact__trade">Automotive Detailing</div>
    <div class="contact__phone">0400 123 456</div>
    <div class="contact__email">bookings@crestlinedetail.com</div>
  </div>

  <svg class="icon-rail" viewBox="0 0 32 160" aria-hidden="true">
    <line x1="16" y1="28" x2="16" y2="132" stroke="#fff" stroke-width="1.5"/>
    <g fill="none" stroke="#fff" stroke-width="1.6">
      <circle cx="16" cy="14" r="12" fill="#3146a3"/>
      <circle cx="16" cy="94" r="12" fill="#3146a3"/>
      <circle cx="16" cy="136" r="12" fill="#3146a3"/>
    </g>
    <g fill="#fff">
      <circle cx="16" cy="10" r="4"/>
      <path d="M9 21a7 6 0 0 1 14 0z"/>
      <path d="M11 88c1-1 3-1 4 1l-1 3c1 2 2 3 4 4l3-1c2 1 2 3 1 4-2 2-5 2-8-1s-5-7-3-10z"/>
      <rect x="9" y="131" width="14" height="10" rx="1"/>
    </g>
    <path d="M9 131l7 6 7-6" fill="none" stroke="#3146a3" stroke-width="1.4"/>
  </svg>

  <div class="address">
    <svg width="10" height="14" viewBox="0 0 10 14" aria-hidden="true">
      <path d="M5 0a5 5 0 0 1 5 5c0 4-5 9-5 9S0 9 0 5a5 5 0 0 1 5-5z" fill="#fff"/>
      <circle cx="5" cy="5" r="2" fill="#3146a3"/>
    </svg>
    <span>Unit 4/22 Harbour Lane Westfield</span>
  </div>
</section>

<section class="card card--front">
  <div class="front-brand">
    <span class="brand-dot"></span>
    <span class="brand-name">Crestline Detail</span>
  </div>
  <svg class="wave" viewBox="0 0 540 140" preserveAspectRatio="none" aria-hidden="true">
    <path d="M0 30 C150 20 260 40 360 80 C430 110 480 130 500 140 L0 140 Z" fill="#fff"/>
    <path d="M0 58 C140 50 250 70 340 105 C390 122 420 132 440 140 L0 140 Z" fill="#3146a3"/>
    <path d="M0 85 C120 80 220 100 300 130 L320 140 L0 140 Z" fill="#fff"/>
  </svg>
</section>

</body>
</html>
```